Kalmoret Windham & Associates

We would like a simple, professional business card using a similar font to our logo.

Industry/Entity Type

Law Firm

Contact Information for Business Card

Martin Kalmoret, Esq. 47 Tillman Lane, 2nd Floor Brindlewood, CT 06999 Office: 781.555.0143 Cell: 508.555.0196 Email: marty@kwfirmma.com kalmoretwindhamlaw.com

Font styles to use
Other font styles liked:
• We would like to use the fonts used in the logo or similar

Colors
0054AA
0677BA
7BADD7
CADEEF
E8F1F8

Requirements
Must have
• We would like the fonts to match the logo
Nice to have
• not too much design- very simple and professional business card. I added a picture of a business card that I tried to start but I am not a designer! Hopefully it will help with the address and phone numbers and kind of what we are looking for.

```html
<!DOCTYPE html>
<html lang="en">
<head>
<meta charset="utf-8">
<title>Kalmoret Windham &amp; Associates – Business Card</title>
<link rel="stylesheet" href="https://fonts.googleapis.com/css2?family=Cinzel:wght@600&family=Arimo:wght@400;700&display=swap">
<style>
  :root {
    --backdrop: #e4e4e2;
    --card: #353535;
    --ink: #ffffff;
    --ink-soft: #e9e9e9;
    --shadow: rgba(0,0,0,0.28);
  }
  * { box-sizing: border-box; margin: 0; padding: 0; }
  html, body { width: 1200px; height: 801px; overflow: hidden; }
  body {
    background: var(--backdrop);
    display: flex;
    align-items: center;
    justify-content: center;
    gap: 60px;
    font-family: "Arimo", Arial, sans-serif;
  }
  .card {
    position: relative;
    width: 525px;
    height: 300px;
    background: var(--card);
    box-shadow: 0 14px 30px var(--shadow);
    color: var(--ink);
  }
  .brand {
    display: flex;
    align-items: center;
  }
  .brand-square {
    background: var(--ink);
  }
  .brand-rule {
    width: 1.5px;
    background: var(--ink);
  }
  .brand-name {
    font-family: "Cinzel", "Times New Roman", serif;
    font-weight: 600;
    color: var(--ink);
    line-height: 0.95;
    letter-spacing: 0.5px;
  }

  /* Front: contact side */
  .card-front .brand {
    position: absolute;
    left: 30px;
    top: 34px;
  }
  .card-front .brand-square { width: 78px; height: 52px; }
  .card-front .brand-rule { height: 62px; margin: 0 12px; }
  .card-front .brand-name { font-size: 15px; }

  .address {
    position: absolute;
    right: 32px;
    top: 34px;
    text-align: right;
    font-size: 13px;
    line-height: 1.35;
    color: var(--ink-soft);
  }
  .person {
    position: absolute;
    left: 30px;
    top: 134px;
    font-weight: 700;
    font-size: 17px;
    letter-spacing: 0.3px;
  }
  .contact-list {
    position: absolute;
    left: 30px;
    bottom: 30px;
    list-style: none;
    font-size: 13px;
    line-height: 1;
    color: var(--ink-soft);
  }
  .contact-list li {
    display: flex;
    align-items: center;
    gap: 8px;
    margin-top: 7px;
  }
  .contact-list svg {
    width: 12px;
    height: 12px;
    flex: none;
  }

  /* Back: brand side */
  .card-back {
    display: flex;
    align-items: center;
    justify-content: center;
  }
  .card-back .brand-square { width: 160px; height: 100px; }
  .card-back .brand-rule { height: 130px; margin: 0 20px; }
  .card-back .brand-name { font-size: 27px; }
</style>
</head>
<body>

  <section class="card card-front" aria-label="Business card, contact side">
    <div class="brand">
      <span class="brand-square" aria-hidden="true"></span>
      <span class="brand-rule" aria-hidden="true"></span>
      <p class="brand-name">Kalmoret<br>Windham<br>&amp; Associates</p>
    </div>

    <p class="address">47 Tillman Lane<br>2nd Floor Brindlewood<br>CT 06999</p>

    <p class="person">Martin Kalmoret, Esq.</p>

    <ul class="contact-list">
      <li>
        <svg viewBox="0 0 12 12" aria-hidden="true"><path fill="#fff" d="M2.4 1l2 2.2-1 1.2c.6 1.4 1.8 2.6 3.2 3.2l1.2-1 2.2 2-1.2 1.6C4.6 10 2 7.4 1 3.2z"/></svg>
        781.555.0143
      </li>
      <li>
        <svg viewBox="0 0 12 12" aria-hidden="true"><rect x="3" y="0.8" width="6" height="10.4" rx="1" fill="none" stroke="#fff" stroke-width="1.2"/><circle cx="6" cy="9.3" r="0.7" fill="#fff"/></svg>
        508.555.0196
      </li>
      <li>
        <svg viewBox="0 0 12 12" aria-hidden="true"><rect x="0.6" y="2.2" width="10.8" height="7.6" fill="#fff"/><path d="M0.6 2.2L6 6.6l5.4-4.4" fill="none" stroke="#353535" stroke-width="1"/></svg>
        marty@kwfirmma.com
      </li>
      <li>
        <svg viewBox="0 0 12 12" aria-hidden="true"><circle cx="6" cy="6" r="5.2" fill="none" stroke="#fff" stroke-width="1.2"/><ellipse cx="6" cy="6" rx="2.2" ry="5.2" fill="none" stroke="#fff" stroke-width="1"/><path d="M0.8 6h10.4" stroke="#fff" stroke-width="1"/></svg>
        www.kalmoretwindhamlaw.com
      </li>
    </ul>
  </section>

  <section class="card card-back" aria-label="Business card, brand side">
    <div class="brand">
      <span class="brand-square" aria-hidden="true"></span>
      <span class="brand-rule" aria-hidden="true"></span>
      <p class="brand-name">Kalmoret<br>Windham<br>&amp; Associates</p>
    </div>
  </section>

</body>
</html>
```